Building company buisness cards

We are looking for a sharp modern new look for our business cards.We are a New Zealand based company that specialises in house and land packages.We have attached a photo of the current logo and would like to see if it can be improved somehow if needed.We are open to any colours but we have chosen Black and White at this stage. Feel free to change the font and make the logo smarter looking.Play with the colours and see what looks best.We want a card that looks so good know one will want to throw it away!

Target Market(s)

Building profesonals, home buyers

Industry/Entity Type

Building

Contact Information for Business Card

Derek Haskins
0274930268
derekh@stonerange.co.nz

Font styles to use
Serif
Sans Serif

Colors

Designer to choose colors to be used in the design.

Requirements
Must have
• Just the logo on one side and details on the other
• Clean simple looking card
Nice to have
• Round corners and detail like raised or spot UV
• Something that stands out
Should not have
• To title needed, Director etc

```html
<!DOCTYPE html>
<html lang="en">
<head>
<meta charset="utf-8">
<title>Stonerange business card</title>
<link href="https://fonts.googleapis.com/css2?family=Playfair+Display:wght@700&family=PT+Serif:wght@400;700&family=Montserrat:wght@400&display=swap" rel="stylesheet">
<style>
  :root{
    --backdrop:#939598;
    --card:#0b0b0c;
    --card-front:#0d0d0e;
    --emboss:#2b2b2d;
    --name-grey:#5b5c5e;
    --white:#ffffff;
  }
  *{margin:0;padding:0;box-sizing:border-box}
  html,body{width:1029px;height:1200px;overflow:hidden;background:var(--backdrop)}
  .sheet{position:relative;width:1029px;height:1200px}
  .card{position:absolute;left:79px;width:876px;height:502px;border-radius:25px;background:var(--card);overflow:hidden}
  .card--front{top:87px;background:var(--card-front)}
  .card--back{top:616px}

  .front-texture{position:absolute;inset:0;background:radial-gradient(circle at 50% 50%,#111112 0%,#0c0c0d 100%)}
  .wordmark{position:absolute;font-family:"Playfair Display",Georgia,serif;font-weight:700;line-height:1}

  .card--front .wordmark{left:0;right:0;top:0;bottom:0;display:flex;align-items:center;justify-content:center;font-size:78px;color:var(--emboss)}

  .holder{position:absolute;left:116px;top:168px;font-family:"PT Serif",Georgia,serif;font-weight:700;font-size:27px;letter-spacing:1px;color:var(--name-grey);text-transform:uppercase}
  .contact{position:absolute;left:112px;list-style:none;font-family:"PT Serif",Georgia,serif;font-size:19px;letter-spacing:.8px;color:var(--white);text-transform:uppercase}
  .contact li{display:flex;align-items:center;gap:14px;height:28px}
  .contact--phone{top:266px}
  .contact--mail{top:312px}
  .contact svg{width:20px;height:18px;flex:none}
  .divider{position:absolute;left:497px;top:167px;width:2px;height:169px;background:var(--white)}

  .card--back .wordmark{left:556px;top:228px;font-size:38px;color:var(--white)}
  .tagline{position:absolute;left:559px;top:273px;font-family:"Montserrat",Arial,sans-serif;font-size:10.5px;color:var(--white)}
</style>
</head>
<body>
<main class="sheet">
  <section class="card card--front" aria-label="Card front">
    <div class="front-texture" role="img" aria-label="Subtle tone-on-tone repeating pattern across the card"></div>
    <div class="wordmark">Stonerange</div>
  </section>

  <section class="card card--back" aria-label="Card back">
    <h1 class="holder">Derek Haskins</h1>
    <ul class="contact contact--phone">
      <li>
        <svg viewBox="0 0 20 18" aria-hidden="true"><path d="M4 1.5l3 3.2-1.6 1.8c.9 2.3 2.6 4.2 4.8 5.4l1.8-1.6 3.3 2.9-1.8 2.6C8.5 15.5 3.6 10 2.2 3.6z" fill="#fff"/></svg>
        <span>0274930268</span>
      </li>
    </ul>
    <ul class="contact contact--mail">
      <li>
        <svg viewBox="0 0 20 18" aria-hidden="true"><rect x="1" y="3" width="18" height="12" fill="#fff"/><path d="M1 3l9 7 9-7M1 15l6.5-5.5M19 15l-6.5-5.5" stroke="#0b0b0c" stroke-width="1.2" fill="none"/></svg>
        <span>derekh@stonerange.co.nz</span>
      </li>
    </ul>
    <div class="divider" aria-hidden="true"></div>
    <div class="wordmark">Stonerange</div>
    <p class="tagline">Built around your life.</p>
  </section>
</main>
</body>
</html>
```